Harlow Stonefield Civil Construction website design

We want a Bold website to promote our Heavy Civil Construction company, We would like an organic / tangible feel to the site. The pictures will be over saturated so they pop. We need to be able to easliy upload new projects and pictures on a regular basis.
Home page will have a full screen width image, "home page image" with silhouette and logo. It will also have about us area and picture
Page 2 will be Project Gallery with pictures in project folders
Page 3 will be an employment application form and submission
Page 4 will be Contact Us
Target Market(s)
Construction indusrty
Industry/Entity Type
Contractor
Coding
Coded - Design and coding required
Number of Pages Required
4 page
Font styles to use
Other font styles liked:
- Hypatia Sans Pro Light
Look and feel

```html
<!DOCTYPE html>
<html lang="en">
<head>
<meta charset="UTF-8">
<title>Harlow Stonefield Civil Construction</title>
<link rel="stylesheet" href="https://fonts.googleapis.com/css2?family=Poppins:wght@300;400;500;600&family=Chakra+Petch:wght@700&display=swap">
<style>
  :root {
    --brand-blue: #3752a6;
    --ink: #2a2a2a;
    --muted: #444;
    --white: #ffffff;
    --label-bg: rgba(40, 40, 40, 0.72);
    --card-shadow: 0 2px 8px rgba(0,0,0,0.12);
  }
  * { margin: 0; padding: 0; box-sizing: border-box; }
  html, body { width: 907px; height: 1200px; overflow: hidden; background: var(--white); }
  body { position: relative; font-family: "Poppins", sans-serif; color: var(--ink); }

  .site-header { position: absolute; left: 0; top: 0; width: 907px; height: 67px; }
  .brand { position: absolute; left: 107px; top: 14px; display: flex; align-items: center; gap: 7px; }
  .brand-square { width: 30px; height: 30px; background: var(--brand-blue); }
  .brand-name { color: var(--brand-blue); font-weight: 500; font-size: 12px; line-height: 14px; letter-spacing: 0.6px; text-transform: uppercase; }
  .main-nav a { position: absolute; top: 36px; font-size: 11px; color: var(--ink); text-decoration: none; }
  .main-nav a.active { color: var(--brand-blue); font-weight: 500; }

  .hero { position: absolute; left: 0; top: 67px; width: 907px; height: 344px;
    background: linear-gradient(180deg, #6c6f91 0%, #55586f 40%, #3b3d4b 72%, #15151a 88%, #050506 100%); }
  .hero-title { position: absolute; left: 0; top: 97px; width: 907px; text-align: center; color: var(--white);
    font-weight: 400; font-size: 28px; line-height: 35px; }

  .about-photo { position: absolute; left: 107px; top: 465px; width: 360px; height: 266px;
    background: linear-gradient(180deg, #2f6db3 0%, #6e9dd0 38%, #a8845a 55%, #7a6048 100%); }
  .about-card { position: absolute; left: 440px; top: 491px; width: 360px; height: 214px; background: var(--white);
    box-shadow: var(--card-shadow); padding: 12px 10px 0 20px; }
  .about-title { font-family: "Chakra Petch", sans-serif; font-weight: 700; font-size: 33px; line-height: 38px; color: var(--brand-blue); }
  .about-text { margin-top: 5px; font-size: 9.6px; line-height: 20.2px; color: var(--ink); }
  .contact-row { display: flex; align-items: center; margin-top: 5px; font-size: 11px; font-weight: 500; }
  .contact-item { display: flex; align-items: center; gap: 5px; margin-right: 24px; }
  .cta { display: inline-block; margin-top: 8px; margin-left: -5px; background: var(--brand-blue); color: var(--white);
    font-weight: 500; font-size: 12px; padding: 6px 8px; box-shadow: 0 3px 4px rgba(0,0,0,0.25); }

  .section-title { position: absolute; left: 0; top: 780px; width: 907px; text-align: center; font-size: 31px; font-weight: 400;
    color: var(--brand-blue); text-shadow: 0 2px 3px rgba(55,82,166,0.3); }
  .work-tile { position: absolute; top: 839px; width: 163px; height: 209px; }
  .work-label { position: absolute; left: 0; top: 89px; width: 163px; height: 31px; background: var(--label-bg);
    display: flex; align-items: center; gap: 4px; padding-left: 8px; color: var(--white); font-size: 11.5px; font-weight: 500; white-space: nowrap; }
  .label-square { width: 11px; height: 11px; border: 1.5px solid var(--white); flex: none; }

  .footer-brand { position: absolute; left: 0; top: 1104px; width: 907px; display: flex; justify-content: center; align-items: center; gap: 6px; }
  .footer-brand .brand-square { width: 24px; height: 24px; }
  .footer-brand .brand-name { font-size: 10px; line-height: 12px; }
  .footer-nav a { position: absolute; top: 1145px; font-size: 11px; color: var(--ink); text-decoration: none; }
  .copyright { position: absolute; left: 0; top: 1173px; width: 907px; height: 27px; background: var(--brand-blue); color: var(--white);
    font-size: 10.5px; text-align: center; line-height: 27px; }
</style>
</head>
<body>
  <header class="site-header">
    <div class="brand">
      <div class="brand-square"></div>
      <div class="brand-name">Harlow Stonefield<br>Civil Construction</div>
    </div>
    <nav class="main-nav">
      <a class="active" href="#" style="left:525px">Home</a>
      <a href="#" style="left:580px">Project Gallery</a>
      <a href="#" style="left:679px">Careers</a>
      <a href="#" style="left:742px">Contact Us</a>
    </nav>
  </header>

  <section class="hero" role="img" aria-label="Dusk sky over a construction site with silhouettes of an excavator, dozer and haul truck">
    <h1 class="hero-title">We Provide Reliable And Qualitative<br>Construction</h1>
  </section>

  <div class="about-photo" role="img" aria-label="Surveyor in hard hat and safety vest beside a tripod level on a graded site, dozer and mountains behind"></div>
  <section class="about-card">
    <h2 class="about-title">About Us</h2>
    <p class="about-text">Lorem ipsum dolor sit amet, consectetuer adipiscing elit, sed diam nonummy nibh euismod tincidunt ut laoreet dolore magna aliquam erat volutpat. Ut wisi enim ad minim veniam, quis nostrud exerci tation ullamcorper suscipit lobortis.</p>
    <div class="contact-row">
      <span class="contact-item">
        <svg width="16" height="16" viewBox="0 0 24 24" fill="none" stroke="#3752a6" stroke-width="1.5"><path d="M5 3h4l2 5-2.5 1.5a11 11 0 0 0 6 6L16 13l5 2v4a2 2 0 0 1-2 2A16 16 0 0 1 3 5a2 2 0 0 1 2-2z"/><path d="M15 3a6 6 0 0 1 6 6M15 7a2 2 0 0 1 2 2"/></svg>
        555.014.2290
      </span>
      <span class="contact-item">
        <svg width="16" height="16" viewBox="0 0 24 24" fill="none" stroke="#3752a6" stroke-width="1.5"><path d="M3 10l9-7 9 7v11H3z"/><path d="M3 10l9 6 9-6"/><path d="M7 7h10v6"/></svg>
        inquiry@hscivilworks.com
      </span>
    </div>
    <span class="cta">Contact Us Today</span>
  </section>

  <h2 class="section-title">Type of Work We Do</h2>

  <div class="work-tile" style="left:107px; background:linear-gradient(180deg,#5f6f52 0%,#3e5a33 45%,#2d4a2a 75%,#1f3a26 100%)" role="img" aria-label="Aerial view of wooded land development beside a pond">
    <div class="work-label"><span class="label-square"></span>Land Development</div>
  </div>
  <div class="work-tile" style="left:283px; background:linear-gradient(180deg,#8a9a6c 0%,#b8b4aa 30%,#8b7a55 55%,#3a3228 100%)" role="img" aria-label="Yellow loader working in a utility trench">
    <div class="work-label"><span class="label-square"></span>Underground Utilities</div>
  </div>
  <div class="work-tile" style="left:462px; background:linear-gradient(180deg,#3d7ad0 0%,#6ea1e0 35%,#d6a23a 55%,#5b4636 100%)" role="img" aria-label="Yellow excavator grading soil under a blue sky">
    <div class="work-label"><span class="label-square"></span>Excavation &amp; Grading</div>
  </div>
  <div class="work-tile" style="left:637px; background:linear-gradient(90deg,#4d5a48 0%,#6a7560 45%,#8c9196 60%,#7b8288 100%)" role="img" aria-label="Aerial view of a stabilized channel running beside a multi-lane road">
    <div class="work-label"><span class="label-square"></span>Channel Stabilization</div>
  </div>

  <footer>
    <div class="footer-brand">
      <div class="brand-square"></div>
      <div class="brand-name">Harlow Stonefield<br>Civil Construction</div>
    </div>
    <nav class="footer-nav">
      <a href="#" style="left:313px">Home</a>
      <a href="#" style="left:362px">Project Gallery</a>
      <a href="#" style="left:461px">Careers</a>
      <a href="#" style="left:524px">Contact Us</a>
    </nav>
    <div class="copyright">Copyright © 2019 Harlow Stonefield Civil Construction. All Rights Reserved.</div>
  </footer>
</body>
</html>
```